Looking for a clean, modern, and professional business card design that reflects Valtrim Systems

The design should include the company logo, contact details, and align with our brand identity. Please use a sophisticated and minimalist style, incorporating [specific colors, if applicable]. Creativity is welcome, but the card must maintain a polished and professional appearance.

Details to Include:

Name: Gavin Trelowe
Title: VP Sales / Operations
Company: Valtrim Systems
Phone: 483.216.7705
Email: gavin@valtrimsystems-example.com
Website: www.valtrimsystems-example.com

```html
<!DOCTYPE html>
<html lang="en">
<head>
<meta charset="utf-8">
<title>Valtrim Systems business card</title>
<link href="https://fonts.googleapis.com/css2?family=Montserrat:wght@400;500;700&display=swap" rel="stylesheet">
<style>
  :root {
    --bg: #e4e2e3;
    --card: #ffffff;
    --brand-blue: #3a72b0;
    --ink: #1d1d1f;
    --text: #2a2a2a;
  }
  * { margin: 0; padding: 0; box-sizing: border-box; }
  html, body { width: 1200px; height: 1108px; overflow: hidden; }
  body { background: var(--bg); font-family: "Montserrat", sans-serif; position: relative; }

  .card { position: absolute; background: var(--card); }
  .card__band { position: absolute; left: 0; right: 0; bottom: 0; height: 20px; background: var(--brand-blue); }

  .card--front { left: 236px; top: 61px; width: 740px; height: 451px; }
  .card--back  { left: 228px; top: 576px; width: 755px; height: 444px; }

  .wordmark { position: absolute; display: flex; align-items: center; color: var(--ink); font-weight: 700; white-space: nowrap; }
  .wordmark__mark { background: var(--brand-blue); flex: none; }

  .card--front .wordmark { left: 100px; top: 229px; font-size: 22px; gap: 9px; }
  .card--front .wordmark__mark { width: 14px; height: 14px; }

  .card--back .wordmark { left: 0; right: 0; top: 206px; justify-content: center; font-size: 54px; gap: 20px; }
  .card--back .wordmark__mark { width: 34px; height: 34px; }

  .divider { position: absolute; left: 358px; top: 172px; width: 2px; height: 154px; background: var(--brand-blue); }

  .contact { position: absolute; left: 372px; top: 170px; }
  .contact__name { color: var(--brand-blue); font-weight: 700; font-size: 26px; line-height: 1.15; }
  .contact__title { color: var(--text); font-weight: 500; font-size: 16px; margin-top: 2px; margin-left: 2px; }
  .contact__list { list-style: none; margin-top: 16px; }
  .contact__item { display: flex; align-items: center; gap: 12px; font-size: 16px; color: var(--text); height: 33px; }
  .contact__icon { width: 17px; height: 17px; fill: var(--brand-blue); flex: none; margin-left: 2px; }
</style>
</head>
<body>

<section class="card card--front">
  <div class="wordmark"><span class="wordmark__mark"></span>Valtrim Systems</div>
  <div class="divider"></div>
  <div class="contact">
    <h1 class="contact__name">Gavin Trelowe</h1>
    <p class="contact__title">VP Sales / Operations</p>
    <ul class="contact__list">
      <li class="contact__item">
        <svg class="contact__icon" viewBox="0 0 24 24" aria-hidden="true"><path d="M6.6 10.8a15.1 15.1 0 0 0 6.6 6.6l2.2-2.2c.3-.3.7-.4 1-.2 1.1.4 2.3.6 3.6.6.6 0 1 .4 1 1V20c0 .6-.4 1-1 1A17 17 0 0 1 3 4c0-.6.4-1 1-1h3.5c.6 0 1 .4 1 1 0 1.3.2 2.5.6 3.6.1.3 0 .7-.2 1z"/></svg>
        483.216.7705
      </li>
      <li class="contact__item">
        <svg class="contact__icon" viewBox="0 0 24 24" aria-hidden="true"><path d="M3 5h18v2.2l-9 5.6-9-5.6zM3 9.5l9 5.6 9-5.6V19H3z"/></svg>
        gavin@valtrimsystems-example.com
      </li>
      <li class="contact__item">
        <svg class="contact__icon" viewBox="0 0 24 24" aria-hidden="true"><path d="M12 2a10 10 0 1 0 0 20 10 10 0 0 0 0-20zm-1 17.9A8 8 0 0 1 4.2 10.5L9 15.3v1a2 2 0 0 0 2 2zm6.9-2.5a2 2 0 0 0-1.9-1.4h-1v-3a1 1 0 0 0-1-1H8v-2h2a1 1 0 0 0 1-1V7h2a2 2 0 0 0 2-2v-.4a8 8 0 0 1 2.9 12.8z"/></svg>
        www.valtrimsystems-example.com
      </li>
    </ul>
  </div>
  <div class="card__band"></div>
</section>

<section class="card card--back">
  <div class="wordmark"><span class="wordmark__mark"></span>Valtrim Systems</div>
  <div class="card__band"></div>
</section>

</body>
</html>
```